Homepage für Unternehmensberatung
Zielgruppe
Wir sind eine Unternehmensberatung mit einem klaren Branchenfokus auf Banken / Finanzdienstleister.
Unsere Dienstleistungsprodukte lassen sich grob in folgende Themencluster unterteilen:
1)Strategieentwicklung
o IT-Strategie, IT-Architektur, IT-Bebauungsplan
2) Projektmanagement
o Projektportfoliomgmt., Programmmgmt., Projektmanagement, Projektcontrolling
3) Fachberatung
o Bankfachliche IT- Beratung mit Schwerpunkten Kredit, Wertpapiergeschäft,
Bankenaufsichtsrecht, Liquiditätsmanagement
o Anforderungsmanagement inkl. Aufbau von Bewertungs- und Priorisierungsmethoden
4) Prozessberatung/-optimierung
o Prozessanalyse, Prozessdesign, Prozessdokumentation
o Prozessoptimierung auf Basis etablierter Messmethoden
Unser Firmenname Morgenlichtwerk hat für uns eine Doppelbedeutung:
1. Im Außenverhältnis: Wir verstehen uns als Morgenlichtwerk unserer Kunden
2. Im Innenverhältnis: Wir pflegen einen partnerschaftlichen Umgang mit unseren
Mitarbeitern (Teamarbeit)
Aktuell sind wir ein kleines aber feines Team von erfahrenen und hochmotivierten Kollegen. Unsere Mitarbeiter sind ehemalige Führungskräfte sowie erfahrenen Unternehmensberater.
Aufgabenstellung
Entwurf / Design von 2 Seiten:
1. Seite / Startseite:
Simple und elegante Darstellung der oben genannten 4 Themencluster (z.B. Bild/Piktogramm, Textkasten) sowie einer Navigationsmöglichkeit zu folgenden Detailsichten:
• Unternehmen
• Beratungsangebot (siehe Themencluster)
• Partnerunternehmen
• Kontakt
2. Seite / 2. Ebene:
Entwurf einer Möglichkeit zur Erläuterung/Darstellung von Inhalten der Startseite.
Die Themencluster sollten auf jeder Ebene immer „anklickbar“/ zu sehen sein.
Logo
Das angehängte Logo ist in die Website einzubinden. Stil und Farben sollen übernommen werden bzw. sind Basis für das Design.
Lizenzen
Lizenz für eingesetzte Fotos und Illustrationen soll enthalten / Open-Source sein. Wenn nicht dann bitte zusätzliche Kosten angeben.

```html
<!DOCTYPE html>
<html lang="en">
<head>
<meta charset="utf-8">
<title>Morgenlichtwerk – Consulting</title>
<link href="https://fonts.googleapis.com/css2?family=Lato:wght@300;400;700&family=Ubuntu:wght@400;500&family=Noto+Serif:wght@400&display=swap" rel="stylesheet">
<style>
:root{
  --brand:#2f7fb5;
  --brand-dark:#2d5473;
  --nav-pill:#3a8dc5;
  --card:#72a9ca;
  --heading-light:#5b9ac4;
  --text:#333;
  --band:#f4f6f8;
  --field:#f2f3f4;
  --send:#86b8d8;
  --footer:#5d6770;
  --footer-text:#dfe3e6;
  --tag:#484e54;
}
*{box-sizing:border-box;margin:0;padding:0}
html,body{width:1029px;height:1200px;overflow:hidden;background:#fff}
body{font-family:'Lato',sans-serif;color:var(--text);position:relative}
.topline{position:absolute;left:0;top:0;width:1029px;height:3px;background:var(--brand)}
.header{position:absolute;top:3px;left:0;width:1029px;height:69px}
.brand{position:absolute;left:76px;top:10px;display:flex;align-items:center;gap:10px}
.brand-dot{width:50px;height:50px;border-radius:50%;background:var(--brand)}
.brand-name{font-family:'Lato',sans-serif;font-weight:400;font-size:22px;color:var(--brand);letter-spacing:.3px}
.nav{position:absolute;top:18px;left:543px;display:flex;font-size:9.5px;font-weight:400}
.nav a{display:block;color:#222;text-decoration:none;height:24px;line-height:24px;padding:0 12px}
.nav a.active{background:var(--nav-pill);color:#fff;border-radius:4px;margin-right:8px}
.nav a:nth-child(n+2){margin-right:6px}
.hero{position:absolute;top:72px;left:0;width:1029px;height:433px;background:linear-gradient(90deg,#c8cdd2 0%,#d9dde1 30%,#eceef1 55%,#f1f3f6 100%)}
.hero-photo{position:absolute;left:0;top:0;width:580px;height:433px;background:linear-gradient(100deg,#7a8a99 0%,#b9c2cb 40%,#d9c8b3 75%,rgba(236,238,241,0) 100%)}
.hero-title{position:absolute;left:569px;top:152px;font-family:'Noto Serif',serif;font-size:29px;color:var(--brand-dark);white-space:nowrap}
.hero-sub{position:absolute;left:575px;top:198px;font-family:'Noto Serif',serif;font-size:17px;color:var(--brand-dark);display:flex;align-items:center;gap:5px}
.hero-sub .tag{background:var(--tag);color:#fff;padding:3px 11px;font-size:17px}
.focus{position:absolute;top:505px;left:0;width:1029px;height:93px;background:var(--band);text-align:center;font-family:'Ubuntu',sans-serif;color:var(--brand-dark);border-top:1px solid #e7eaed;border-bottom:1px solid #e7eaed}
.focus h1{font-weight:500;font-size:28px;margin-top:11px}
.focus p{font-size:21px;margin-top:1px}
.services{position:absolute;top:639px;left:75px;display:flex;gap:9px}
.card{width:213px;height:260px;background:var(--card);border-radius:2px;color:#fff;text-align:center;padding-top:24px}
.icon{width:96px;height:96px;margin:0 auto;border-radius:50%;border:3px solid #fff;padding:4px}
.icon-inner{width:100%;height:100%;border-radius:50%;background:var(--card);display:flex;align-items:center;justify-content:center}
.card h2{font-size:14.5px;font-weight:400;margin-top:22px;letter-spacing:.1px}
.card p{font-size:9.6px;line-height:13.7px;margin:13px 7px 0;font-weight:400}
.section-title{font-size:21px;font-weight:300;color:var(--heading-light)}
.address{position:absolute;left:79px;top:924px;width:200px}
.address h3{font-size:14px;font-weight:700;color:#222;margin-top:12px}
.address .street{font-size:10.5px;line-height:14.5px;margin-top:6px;color:#222}
.contact-list{position:absolute;left:81px;top:1061px;font-size:10px;line-height:14.5px;color:#222;border-collapse:collapse}
.contact-list td:first-child{width:49px}
.contact-list a{color:#222}
.map{position:absolute;left:298px;top:967px;width:260px;height:151px;border:1px solid #d6d6d6;background:#ece8df}
.ask{position:absolute;left:581px;top:924px;width:372px}
.field{position:absolute;background:var(--field);border-radius:2px;font-size:10px;color:#aaa;padding:9px 12px}
.send{position:absolute;left:581px;top:1083px;width:179px;height:33px;background:var(--send);color:#fff;font-size:17px;text-align:center;line-height:33px;border-bottom:2px solid #6aa3c8}
.footer{position:absolute;left:0;top:1156px;width:1029px;height:44px;background:var(--footer);color:var(--footer-text);font-size:10.5px}
.footer-nav{position:absolute;left:78px;top:15px}
.footer-nav span{margin:0 7px}
.copyright{position:absolute;right:75px;top:15px}
</style>
</head>
<body>
<div class="topline"></div>

<header class="header">
  <div class="brand"><div class="brand-dot"></div><span class="brand-name">Morgenlichtwerk</span></div>
  <nav class="nav">
    <a class="active" href="#">HOME</a>
    <a href="#">COMPANY</a>
    <a href="#">CONSULTING</a>
    <a href="#">SERVICE</a>
    <a href="#">PARTNER</a>
    <a href="#">CONTACT</a>
  </nav>
</header>

<section class="hero">
  <div class="hero-photo" role="img" aria-label="Photo of three colleagues working together at a laptop in a bright office"></div>
  <div class="hero-title">We maintain a fair approach</div>
  <div class="hero-sub">with our employees <span class="tag">teamwork</span></div>
</section>

<section class="focus">
  <h1>We are a consultancy, which is specially focused on</h1>
  <p>Banks / Finance services</p>
</section>

<section class="services">
  <article class="card">
    <div class="icon"><div class="icon-inner">
      <svg width="48" height="40" viewBox="0 0 48 40" fill="none" stroke="#fff" stroke-width="2"><rect x="2" y="2" width="44" height="36" rx="2"/><line x1="2" y1="10" x2="46" y2="10"/><circle cx="7" cy="6" r="1" fill="#fff"/><circle cx="11" cy="6" r="1" fill="#fff"/><circle cx="15" cy="6" r="1" fill="#fff"/><rect x="7" y="15" width="12" height="16"/><line x1="7" y1="15" x2="19" y2="31"/><line x1="19" y1="15" x2="7" y2="31"/><line x1="24" y1="16" x2="41" y2="16"/><line x1="24" y1="21" x2="41" y2="21"/><line x1="24" y1="26" x2="41" y2="26"/><line x1="24" y1="31" x2="41" y2="31"/></svg>
    </div></div>
    <h2>STRATEGY DEVELOPMENT</h2>
    <p>Lorem ipsum dolor sit amet, ectetur adipiscing elit. Vivamus eu curs turpis. Nullam vestibulum nisi sit amet viverra hendrerit. Morbi imperdiet tortoacinia tempus. Pellentesque at congue orci.</p>
  </article>
  <article class="card">
    <div class="icon"><div class="icon-inner">
      <svg width="50" height="48" viewBox="0 0 50 48" fill="none" stroke="#fff" stroke-width="2"><rect x="3" y="6" width="30" height="26"/><line x1="18" y1="2" x2="18" y2="6"/><line x1="18" y1="32" x2="10" y2="44"/><line x1="18" y1="32" x2="26" y2="44"/><rect x="9" y="20" width="3" height="8" fill="#fff"/><rect x="15" y="14" width="3" height="14" fill="#fff"/><rect x="21" y="18" width="3" height="10" fill="#fff"/><circle cx="42" cy="10" r="3.5" fill="#fff"/><path d="M37 16h10v16h-3v12h-4V32h-3z" fill="#fff" stroke="none"/><line x1="37" y1="18" x2="30" y2="12"/></svg>
    </div></div>
    <h2>PROJECT MANAGEMENT</h2>
    <p>Lorem ipsum dolor sit amet, ectetur adipiscing elit. Vivamus eu curs turpis. Nullam vestibulum nisi sit amet viverra hendrerit. Morbi imperdiet tortoacinia tempus. Pellentesque at congue orci.</p>
  </article>
  <article class="card">
    <div class="icon"><div class="icon-inner">
      <svg width="56" height="40" viewBox="0 0 56 40" fill="#fff"><circle cx="11" cy="8" r="6"/><circle cx="45" cy="8" r="6"/><path d="M2 38V22a6 6 0 0 1 6-6h8l10 8-4 4-6-4v14z"/><path d="M54 38V22a6 6 0 0 0-6-6h-8l-10 8 4 4 6-4v14z"/></svg>
    </div></div>
    <h2>CONSULTING SERVICES</h2>
    <p>Lorem ipsum dolor sit amet, ectetur adipiscing elit. Vivamus eu curs turpis. Nullam vestibulum nisi sit amet viverra hendrerit. Morbi imperdiet tortoacinia tempus. Pellentesque at congue orci.</p>
  </article>
  <article class="card">
    <div class="icon"><div class="icon-inner">
      <svg width="52" height="46" viewBox="0 0 52 46" fill="#fff"><path d="M4 44c0-10 4-14 8-16-4-3-5-8-5-12 0-7 5-12 11-12s10 5 10 11c0 5-2 10-6 13 4 2 6 7 6 16z"/><path d="M48 44c0-10-4-14-8-16 4-3 5-8 5-12 0-7-5-12-11-12-2 0-3 0-4 1 3 3 4 7 4 11 0 5-2 10-5 13 4 3 5 8 5 15z"/></svg>
    </div></div>
    <h2>CONSULTING &amp; OPTIMIZATION</h2>
    <p>Lorem ipsum dolor sit amet, ectetur adipiscing elit. Vivamus eu curs turpis. Nullam vestibulum nisi sit amet viverra hendrerit. Morbi imperdiet tortoacinia tempus. Pellentesque at congue orci.</p>
  </article>
</section>

<section class="address">
  <h2 class="section-title">Address</h2>
  <h3>Morgenlichtwerk GmbH</h3>
  <div class="street">Lindenhofweg 12<br>Kesselbrunn 48213, DE</div>
</section>
<table class="contact-list">
  <tr><td>Phone:</td><td>+49 301 204 880</td></tr>
  <tr><td>Fax:</td><td>+49 301 204 881</td></tr>
  <tr><td>E-mail:</td><td><a href="#">info@morgenlichtwerk.de</a></td></tr>
  <tr><td>Skype:</td><td>Morgenlichtwerk</td></tr>
</table>
<div class="map" role="img" aria-label="Street map showing the office location"></div>

<section class="ask">
  <h2 class="section-title">Ask a question</h2>
</section>
<div class="field" style="left:581px;top:968px;width:179px;height:27px">Name</div>
<div class="field" style="left:773px;top:968px;width:179px;height:27px">|</div>
<div class="field" style="left:581px;top:1009px;width:371px;height:67px">Your question</div>
<div class="send">SEND</div>

<footer class="footer">
  <div class="footer-nav">Home<span>/</span>Company<span>/</span>Consulting<span>/</span>Service<span>/</span>Partner<span>/</span>Contact</div>
  <div class="copyright">Copyright © 2014 Morgenlichtwerk GmbH.</div>
</footer>
</body>
</html>
```